Professional educational and informative brochures for CPAP alternative treatment for sleep apnea

I am a dentist who practices dental sleep medicine, alternative to CPAP, such as custom-fit oral appliance therapy, laser treatment, and other adjunctive treatments. I need a professional trifold brochure to give directly to patients and physicians. The brochure needs to be educational and informative, and I would also like it to provide some information about me from a marketing standpoint. I had a custom brochure made in the past, more catered for patients, but it looks too crowded with info and hard to read. I need a clean and easy-to-read brochure. It could be tri-fold or quarter-fold. I attached some files on my current brochure, business card, and logos for your review and ideas.
Updates

Nothing really caught my attention. Plus most of them are out of target of what I am looking for. I put more specific info on my project.

Target Market(s)

Referring physicians and self referred patients who seeks CPAP alternative treatments

Industry/Entity Type

Healthcare

Requirements
Must have
• a message that emphasizes that I can provide treatments alternative to CPAP for sleep apnea patients who do not tolerate CPAP
Nice to have
• pictures of each treatments I provide instead of CPAP
Should not have
• a message that confuses people that I am promoting CPAP as a CPAP provider because I am not!

```html
<!DOCTYPE html>
<html lang="en">
<head>
<meta charset="utf-8">
<title>Sleep Apnea Trifold Brochure</title>
<link rel="stylesheet" href="https://fonts.googleapis.com/css2?family=Montserrat:ital,wght@0,400;0,500;0,600;0,700;0,800;1,400;1,500;1,800&display=swap">
<style>
:root{
  --canvas:#ececec;
  --panel-black:#111213;
  --panel-mid:#1b1e22;
  --panel-slate:#2a2f37;
  --orange:#e2661b;
  --cream:#efe1cd;
  --text:#e9e9e9;
  --muted:#bfc1c4;
  --photo-warm:#a8633f;
  --photo-cool:#cfc7c2;
}
*{margin:0;padding:0;box-sizing:border-box}
html,body{width:1200px;height:3000px;overflow:hidden;background:var(--canvas)}
body{position:relative;font-family:"Montserrat",sans-serif;color:var(--text)}
.sheet{position:absolute;left:50px;width:1100px;height:800px;display:grid;grid-template-columns:repeat(3,1fr);box-shadow:0 18px 40px rgba(0,0,0,.18)}
.sheet--outside{top:560px}
.sheet--inside{top:1560px}
.panel{position:relative;overflow:hidden;padding:34px 30px}
.panel--black{background:var(--panel-black)}
.panel--mid{background:var(--panel-mid)}
.panel--slate{background:linear-gradient(160deg,#333843,var(--panel-slate) 60%,#23272e)}
.heading{position:relative;font-weight:700;font-size:15px;line-height:1.25;margin-bottom:14px;color:#fff}
.heading--flag::before{content:"";position:absolute;left:-30px;top:2px;width:16px;height:30px;background:var(--orange)}
.list{list-style:none;font-size:10.4px;line-height:1.42;color:var(--text)}
.list li{position:relative;padding-left:14px}
.list li::before{content:"";position:absolute;left:0;top:4px;width:6px;height:6px;background:var(--orange)}
.list--ring li::before{background:none;border:1.6px solid var(--orange);border-radius:50%;width:7px;height:7px}
.list--spaced li{margin-bottom:7px}
.body{font-size:10.4px;line-height:1.45;color:var(--text);text-align:justify;margin-bottom:10px}
.body--flag{position:relative}
.body--flag::before{content:"";position:absolute;left:-30px;top:1px;width:14px;height:28px;background:var(--orange)}
.clouds{position:absolute;left:0;right:0;bottom:0;height:70px;background:linear-gradient(to top,rgba(239,225,205,.75),rgba(239,225,205,.15) 60%,transparent)}
.star{position:absolute}
.photo{position:absolute;border-radius:50%}
.caption{font-size:10.4px;text-align:center;margin:8px 0 10px}
.badges{display:flex;gap:14px;align-items:center;margin-top:6px}
.badge{background:#e4e4e4}
.moon{position:absolute;left:120px;top:42px}
.cover-title{position:absolute;left:0;right:0;top:468px;text-align:center;font-size:29px;font-weight:400;font-style:italic;letter-spacing:.5px;line-height:1.2;color:#fff;white-space:nowrap}
.cover-title strong{font-weight:800}
.brand{position:absolute;left:0;right:0;top:560px;display:flex;justify-content:center;align-items:center;gap:8px;font-size:13px;font-weight:500;white-space:nowrap}
.brand-dot{width:14px;height:14px;border-radius:50%;background:#fff;flex:none}
.contact{position:absolute;left:0;right:0;top:598px;text-align:center;font-size:12px;line-height:1.4}
.contact .contact-name{font-size:15px;margin-bottom:6px}
.figure{position:absolute;left:141px;top:165px;width:84px;height:555px;border-radius:42px 42px 16px 16px;background:linear-gradient(to bottom,#f1e4d1,#e3d1b8)}
.label{position:absolute;font-size:7px;line-height:1.5;font-weight:600;text-transform:uppercase;color:#fff;white-space:nowrap}
.pointer{position:absolute;height:1px;background:var(--orange)}
.subheading{font-weight:700;font-size:13px;line-height:1.25;margin:18px 0 12px;position:relative}
.subheading--flag::before{content:"";position:absolute;left:-30px;top:1px;width:14px;height:30px;background:var(--orange)}
.center-title{text-align:center;font-weight:700;font-size:14px;line-height:1.25;margin-top:14px}
.footnote{position:absolute;left:30px;right:30px;bottom:28px;font-size:8.4px;font-style:italic;line-height:1.4}
</style>
</head>
<body>

<section class="sheet sheet--outside">
  <div class="panel panel--black">
    <h2 class="heading heading--flag">Signs you may not know<br>you have Sleep Apnea</h2>
    <ul class="list">
      <li>Gasping, choking or snorting during sleep</li>
      <li>Waking up tired despite the full night sleep</li>
      <li>Waking up with dry mouth / sore throat</li>
      <li>Waking up with a headache</li>
      <li>Feeling sleepy or tired during the day</li>
      <li>despite a full night's sleep</li>
      <li>Falling asleep in inappropriate</li>
      <li>situations (movies, church, sitting quietly)</li>
      <li>Problems with memory and concentration</li>
      <li>Being ill-tempered or irritable</li>
      <li>Depression</li>
      <li>Nightmares</li>
      <li>Irregular heartbeat</li>
      <li>Nighttime teeth grinding / tapping</li>
      <li>Worn-down teeth</li>
      <li>Gum disease</li>
      <li>Gum recession</li>
      <li>Acid reflux / GERD</li>
      <li>Frequent nighttime urination</li>
      <li>High Cholesterol</li>
      <li>Sexual dysfunction / Decreased libido</li>
    </ul>
    <h2 class="heading heading--flag" style="margin-top:14px">Signs you may not know<br>you have Sleep Apnea</h2>
    <ul class="list">
      <li>Enlarged tongue, tonsils, uvula, adenoid</li>
      <li>Narrow arches of the mouth</li>
      <li>Misaligned teeth</li>
      <li>Tori (Bony structure above or under the tongue)</li>
      <li>Recessed chin</li>
      <li>Large overbite</li>
      <li>Deep overbite</li>
      <li>Narrow arches of the mouth</li>
      <li>Alcohol consumption</li>
      <li>Smoking</li>
      <li>Genetically predisposed (family history)</li>
      <li>Large neck size (fat or muscles)</li>
      <li>Chronic nasal/sinus congestion</li>
      <li>Asthma</li>
      <li>Menopause including pre and post</li>
      <li>Diabetes</li>
    </ul>
    <svg class="star" style="left:290px;top:280px" width="30" height="30" viewBox="0 0 30 30"><path d="M15 0 L17 13 L30 15 L17 17 L15 30 L13 17 L0 15 L13 13Z" fill="var(--cream)"/></svg>
    <div class="clouds" role="img" aria-label="Soft night clouds along the lower edge"></div>
  </div>

  <div class="panel panel--mid">
    <h2 class="heading">Invest in your health and<br>get a good night rest</h2>
    <p class="body">Sleep apnea is closely linked to several life-threatening conditions, and it could shorten your life span from anywhere between 12–15 years. Treating sleep apnea will improve the quality of life and even help save life.</p>
    <p class="body">Dr. Harrow and her team believe you deserve a good night's sleep. If you are interested in learning more about the cost of treating sleep apnea and how you go about treating sleep apnea, talk to Dr. Harrow and her team. Her entire team cares about not only your oral health but also your overall health. You and your loved ones deserve a good night sleep.</p>
    <svg class="star" style="left:262px;top:258px" width="26" height="26" viewBox="0 0 30 30"><path d="M15 0 L17 13 L30 15 L17 17 L15 30 L13 17 L0 15 L13 13Z" fill="var(--cream)"/></svg>
    <div style="position:relative;width:88px;height:88px;margin:26px auto 0;border-radius:50%;background:radial-gradient(circle at 50% 40%,#4a4f57,#1a1c20)" role="img" aria-label="Portrait photo of Dr. Lena Harrow"></div>
    <p class="caption">Dr. Lena Harrow, DMD, D-ABDSM</p>
    <p class="body">Dr. Lena Harrow graduated from Northfield University School of Dentistry and began practicing in 1999. Throughout her dental career, she has attended countless hours of continuing education to advance her knowledge and skills in dentistry to better serve her patients. She has been always fascinated by the correlation between oral health and systemic disease. Eventually, she realized that a dentist could directly contribute to patients' overall health. By recognizing certain appearances in the mouth, she could screen for sleep apnea which is a life-threatening condition. She became passionate about treating sleep apnea by providing each patient with a custom-fit oral appliance. Today, her passion and focus are to improve patients' sleep and their quality of life.</p>
    <div class="badges">
      <div class="badge" style="width:64px;height:26px;border-radius:3px" role="img" aria-label="Professional academy membership badge"></div>
      <div class="badge" style="width:28px;height:28px;border-radius:50%" role="img" aria-label="Certification seal"></div>
      <div class="badge" style="width:54px;height:22px;border-radius:3px" role="img" aria-label="Professional society badge"></div>
      <div class="badge" style="width:54px;height:22px;border-radius:3px" role="img" aria-label="Sleep medicine association badge"></div>
    </div>
  </div>

  <div class="panel panel--slate">
    <svg class="moon" width="90" height="100" viewBox="0 0 90 100"><path d="M50 6 A46 46 0 1 0 86 74 A38 38 0 1 1 50 6Z" fill="var(--cream)"/></svg>
    <svg class="star" style="left:290px;top:30px" width="26" height="26" viewBox="0 0 30 30"><path d="M15 0 L17 13 L30 15 L17 17 L15 30 L13 17 L0 15 L13 13Z" fill="var(--cream)"/></svg>
    <svg class="star" style="left:316px;top:54px" width="12" height="12" viewBox="0 0 30 30"><path d="M15 0 L17 13 L30 15 L17 17 L15 30 L13 17 L0 15 L13 13Z" fill="var(--cream)"/></svg>
    <svg class="star" style="left:60px;top:160px" width="22" height="22" viewBox="0 0 30 30"><path d="M15 0 L17 13 L30 15 L17 17 L15 30 L13 17 L0 15 L13 13Z" fill="var(--cream)"/></svg>
    <svg class="star" style="left:84px;top:150px" width="10" height="10" viewBox="0 0 30 30"><path d="M15 0 L17 13 L30 15 L17 17 L15 30 L13 17 L0 15 L13 13Z" fill="var(--cream)"/></svg>
    <div class="photo" style="left:68px;top:195px;width:228px;height:228px;background:radial-gradient(circle at 45% 45%,#c99a72,var(--photo-warm) 55%,#5a2f22)" role="img" aria-label="Photo of a woman sleeping peacefully on a pillow"></div>
    <h1 class="cover-title">DO YOU<br>HAVE <strong>SLEEP ARNA?</strong></h1>
    <div class="brand"><span class="brand-dot"></span>Starlit Sleep Solutions</div>
    <div class="contact">
      <p class="contact-name">Starlit Sleep Solutions</p>
      <p>555-014-2290</p>
      <p>200 Example Ave, Suite 4</p>
      <p>Riverton, OR 97000</p>
    </div>
  </div>
</section>

<section class="sheet sheet--inside">
  <div class="panel panel--black" style="padding-top:290px">
    <div class="photo" style="left:-40px;top:-60px;width:330px;height:330px;background:radial-gradient(circle at 55% 55%,#e8ddd6,var(--photo-cool) 55%,#8f8680);box-shadow:0 0 0 8px var(--cream)" role="img" aria-label="Photo of a smiling patient during a dental exam"></div>
    <svg class="star" style="left:300px;top:40px" width="24" height="24" viewBox="0 0 30 30"><path d="M15 0 L17 13 L30 15 L17 17 L15 30 L13 17 L0 15 L13 13Z" fill="var(--cream)"/></svg>
    <svg class="star" style="left:300px;top:420px" width="24" height="24" viewBox="0 0 30 30"><path d="M15 0 L17 13 L30 15 L17 17 L15 30 L13 17 L0 15 L13 13Z" fill="var(--cream)"/></svg>
    <h2 class="heading">What are my options for<br>treating Sleep Apnea?</h2>
    <p class="body" style="text-align:left">There are several options, and it could be alone or combination of the following treatment</p>
    <ul class="list list--spaced" style="font-size:9.6px">
      <li>CPAP (Continuous Positive Airway Pressure) machine</li>
      <li>Surgery (invasive procedure)</li>
      <li>Oral Appliance</li>
      <li>Teeth Alignment<br>(clear aligners such as ClearFit and Smileline)</li>
      <li>Laser Treatment</li>
      <li>Myofunctional Therapy</li>
    </ul>
    <p class="body body--flag" style="margin-top:14px;text-align:left">Oral Appliance, Teeth Alignment, Laser Treatment, and Myofunctional Therapy can be done in a dental office.</p>
    <p class="body">If you have severe sleep apnea, then your first choice will be more likely a device called CPAP (continuous positive airway pressure). However, if you cannot wear or tolerate CPAP for any reasons, another option will be wearing a custom fit oral appliance nightly. You may choose to have an oral appliance alone or in combination with alignment, laser treatment, and myofunctional therapy. Having an oral appliance may be a better option than no treatment at all if you cannot tolerate CPAP.</p>
    <div class="clouds" role="img" aria-label="Soft night clouds along the lower edge"></div>
  </div>

  <div class="panel panel--mid">
    <h2 class="center-title">CONSEQUENCES OF UNTREATED<br>SLEEP APNEA</h2>
    <svg class="star" style="left:320px;top:40px" width="22" height="22" viewBox="0 0 30 30"><path d="M15 0 L17 13 L30 15 L17 17 L15 30 L13 17 L0 15 L13 13Z" fill="var(--cream)"/></svg>
    <svg class="star" style="left:40px;top:520px" width="24" height="24" viewBox="0 0 30 30"><path d="M15 0 L17 13 L30 15 L17 17 L15 30 L13 17 L0 15 L13 13Z" fill="var(--cream)"/></svg>
    <div class="figure" role="img" aria-label="Illustration of a standing human body silhouette"></div>
    <p class="label" style="left:22px;top:150px">Stroke<br>Dementia and Alzheimer<br>Insomnia<br>ADHD</p>
    <span class="pointer" style="left:128px;top:156px;width:44px"></span>
    <p class="label" style="left:250px;top:150px">Sudden death<br>Depression<br>Anxiety disorder<br>Panic attack<br>Weight gain<br>Type 2 diabetes</p>
    <span class="pointer" style="left:196px;top:156px;width:50px"></span>
    <p class="label" style="left:22px;top:290px">Heart disease<br>Heart failure<br>Coronary artery<br>disease<br>High blood pressure</p>
    <span class="pointer" style="left:118px;top:296px;width:62px"></span>
    <p class="label" style="left:250px;top:365px">Acid reflux<br>GERD</p>
    <span class="pointer" style="left:192px;top:371px;width:54px"></span>
    <p class="label" style="left:250px;top:500px">Nocturia<br>Reduced libido<br>Erectile dysfunction<br>Seperate sleeping<br>arrangement<br>with a partner<br>High risk of divorce</p>
    <p class="label" style="left:22px;top:590px">Increased risk of cancer<br>Low immune system<br>Fibromyalgia<br>Restless legs syndrome</p>
    <p class="footnote">Increased risk of car accidents (3–7 times more).<br>Annual medical cost for untreated sleep apnea could be as much as $200,000 per patient per year.</p>
  </div>

  <div class="panel panel--black">
    <svg class="star" style="left:300px;top:26px" width="24" height="24" viewBox="0 0 30 30"><path d="M15 0 L17 13 L30 15 L17 17 L15 30 L13 17 L0 15 L13 13Z" fill="var(--cream)"/></svg>
    <svg class="star" style="left:324px;top:48px" width="10" height="10" viewBox="0 0 30 30"><path d="M15 0 L17 13 L30 15 L17 17 L15 30 L13 17 L0 15 L13 13Z" fill="var(--cream)"/></svg>
    <svg class="star" style="left:30px;top:690px" width="24" height="24" viewBox="0 0 30 30"><path d="M15 0 L17 13 L30 15 L17 17 L15 30 L13 17 L0 15 L13 13Z" fill="var(--cream)"/></svg>
    <h2 class="heading">How do I find out if I have<br>sleep Apnea?</h2>
    <p class="body" style="text-align:left">Many signs of sleep apnea can be recognized during your dental visit. Dr. Harrow and her dental team can help you initiate the sleep study to determine if you have sleep apnea or not.</p>
    <h3 class="subheading subheading--flag">Benefits of Oral<br>Appliances over CPAP</h3>
    <ul class="list list--spaced">
      <li>More comfortable to wear than CPAP</li>
      <li>Easier to clean</li>
      <li>Easier to travel as it is very compact</li>
      <li>Quiet as there is no machine next to you</li>
      <li>No dry mouth, throat or nose</li>
      <li>No bloating or gas from the air pressure</li>
      <li>No monthly maintenance and costs<br>to change hoses and face mask</li>
      <li>Looks much sexier than wearing CPAP<br>(No one wants to look like a space villain in bed)</li>
    </ul>
    <h3 class="subheading subheading--flag">What does the research say about<br>Oral Appliances?</h3>
    <ul class="list list--ring list--spaced">
      <li>A 2022 study found that Oral Appliances can be 94% effective in treating mild to moderate sleep apnea.</li>
      <li>Oral Appliances were 81% successful across all levels of sleep apnea severity in reducing snore and improving the sleep quality and energy.</li>
    </ul>
    <div class="photo" style="left:190px;top:650px;width:260px;height:260px;background:radial-gradient(circle at 40% 35%,#e7c9c9,#c99a9a 50%,#6e5352);box-shadow:0 0 0 8px var(--cream)" role="img" aria-label="Photo of a person asleep wearing a CPAP mask"></div>
  </div>
</section>

</body>
</html>
```